" A EMPRESA VELMORA CASTI DESENVOLVE A MELHOR PALHA ITALIANA DO MERCADO E QUEREMOS DISPONIBILIZAR ESSA VENDA PARA TODO O MERCADO. QUEREMOS VENDER EM MERCADOS, SALÕES DE BELEZA, LANCHONETES, RESTAURANTES ETC. NÃO TEMOS AO CERTO TODOS OS SABORES: SOMENTE O TRADICIONAL É CERTEZA. ESTAMOS EXPERIMENTANDO O SABOR ZUVI, TALVO, DOCE DE LEITE E MEIO AMARGO ,LIMÃO, BRIGADEIRO BRANCO. MAS FICAM AS CORES COMO SUGESTÕES. "

```html
<!DOCTYPE html>
<html lang="pt-BR">
<head>
<meta charset="utf-8">
<title>Velmora Casti — rótulos de palha italiana</title>
<link rel="stylesheet" href="https://fonts.googleapis.com/css2?family=Cinzel:wght@400;700&display=swap">
<style>
  :root {
    --page: #f4f3f1;
    --cream: #f3e6d3;
    --cream-deep: #e6d2b6;
    --stripe: #b8966a;
    --stripe-light: #d8c19d;
    --damask: #eadbc4;
    --brown: #6e4a2e;
    --brown-dark: #4d3220;
    --gold: #a9834f;
    --mint: #a9d9c4;
    --mint-dark: #7fbfa5;
    --ribbon-text: #ffffff;
  }
  * { box-sizing: border-box; margin: 0; padding: 0; }
  html, body { width: 1200px; height: 1200px; overflow: hidden; }
  body {
    background: var(--page);
    display: flex;
    align-items: center;
    justify-content: center;
    gap: 80px;
  }
  .label {
    position: relative;
    width: 460px;
    height: 600px;
    background: linear-gradient(180deg, var(--cream) 0%, var(--cream-deep) 100%);
    box-shadow: 0 10px 30px rgba(80, 55, 30, 0.18);
    overflow: hidden;
  }
  .label__damask {
    position: absolute;
    top: 0; bottom: 0;
    width: 44px;
    background: linear-gradient(180deg, var(--damask), #e2cfb2);
  }
  .label__damask--left { left: 0; }
  .label__damask--right { right: 0; }
  .label__stripe {
    position: absolute;
    top: 0; bottom: 0;
    width: 6px;
    border-left: 2px solid var(--stripe);
    border-right: 1px solid var(--stripe-light);
  }
  .label__stripe--left { left: 48px; }
  .label__stripe--right { right: 48px; }
  .label__flourish {
    position: absolute;
    left: 110px; right: 110px;
    height: 34px;
    border-radius: 50%;
    background: linear-gradient(90deg, transparent, rgba(169, 131, 79, 0.45), transparent);
  }
  .label__flourish--top { top: 70px; }
  .label__flourish--bottom { top: 318px; }
  .brand {
    position: absolute;
    top: 124px; left: 60px; right: 60px;
    height: 180px;
    display: flex;
    align-items: center;
    justify-content: center;
    text-align: center;
  }
  .brand__name {
    font-family: "Cinzel", serif;
    font-weight: 700;
    font-size: 52px;
    line-height: 1.05;
    letter-spacing: 2px;
    color: var(--brown);
  }
  .flavor {
    position: absolute;
    left: 30px; right: 30px;
    bottom: 110px;
    height: 90px;
  }
  .flavor svg { position: absolute; inset: 0; width: 100%; height: 100%; }
  .flavor__name {
    position: absolute;
    inset: 0;
    display: flex;
    align-items: center;
    justify-content: center;
    font-family: "Cinzel", serif;
    font-weight: 400;
    font-size: 34px;
    letter-spacing: 5px;
    color: var(--ribbon-text);
    padding-bottom: 6px;
  }
  .flavor--lemon .ribbon-main { fill: var(--mint); }
  .flavor--lemon .ribbon-tail { fill: var(--mint-dark); }
  .flavor--classic .ribbon-main { fill: var(--brown); }
  .flavor--classic .ribbon-tail { fill: var(--brown-dark); }
  .flavor--classic .flavor__name { font-size: 28px; letter-spacing: 3px; }
</style>
</head>
<body>

  <article class="label label--lemon">
    <div class="label__damask label__damask--left" role="img" aria-label="Faixa lateral com padrão damasco em tons creme"></div>
    <div class="label__damask label__damask--right" role="img" aria-label="Faixa lateral com padrão damasco em tons creme"></div>
    <div class="label__stripe label__stripe--left"></div>
    <div class="label__stripe label__stripe--right"></div>
    <div class="label__flourish label__flourish--top" role="img" aria-label="Arabesco dourado decorativo"></div>
    <header class="brand">
      <h1 class="brand__name">VELMORA<br>CASTI</h1>
    </header>
    <div class="label__flourish label__flourish--bottom" role="img" aria-label="Arabesco dourado decorativo"></div>
    <div class="flavor flavor--lemon">
      <svg viewBox="0 0 400 90" preserveAspectRatio="none" aria-hidden="true">
        <path class="ribbon-tail" d="M0 30 L50 30 L50 80 L0 80 L18 55 Z"/>
        <path class="ribbon-tail" d="M400 30 L350 30 L350 80 L400 80 L382 55 Z"/>
        <path class="ribbon-main" d="M30 18 Q200 38 370 18 L370 72 Q200 92 30 72 Z"/>
      </svg>
      <span class="flavor__name">LIMÃO</span>
    </div>
  </article>

  <article class="label label--classic">
    <div class="label__damask label__damask--left" role="img" aria-label="Faixa lateral com padrão damasco em tons creme"></div>
    <div class="label__damask label__damask--right" role="img" aria-label="Faixa lateral com padrão damasco em tons creme"></div>
    <div class="label__stripe label__stripe--left"></div>
    <div class="label__stripe label__stripe--right"></div>
    <div class="label__flourish label__flourish--top" role="img" aria-label="Arabesco dourado decorativo"></div>
    <header class="brand">
      <h1 class="brand__name">VELMORA<br>CASTI</h1>
    </header>
    <div class="label__flourish label__flourish--bottom" role="img" aria-label="Arabesco dourado decorativo"></div>
    <div class="flavor flavor--classic">
      <svg viewBox="0 0 400 90" preserveAspectRatio="none" aria-hidden="true">
        <path class="ribbon-tail" d="M0 30 L50 30 L50 80 L0 80 L18 55 Z"/>
        <path class="ribbon-tail" d="M400 30 L350 30 L350 80 L400 80 L382 55 Z"/>
        <path class="ribbon-main" d="M30 18 Q200 38 370 18 L370 72 Q200 92 30 72 Z"/>
      </svg>
      <span class="flavor__name">TRADICIONAL</span>
    </div>
  </article>

</body>
</html>
```